Website design for learning and development business

I need a logo for my new business based in Australasia. I am a kiwi who is a creative change maker working in the Learning & development space. I design experiential learning opportunities for businesses to grow and nurture their tribes. I take a holistic look at an organisation and analyse what is needed to build a positive culture with a growth mindset woven into their DNA. I would like to see designs that are based on the following word snaps - creative, interesting, tribal, journey, adaptability, engaging, fluid, architectural, bespoke, courageous, challenging .I have the logo (attached) and I Need a startup business website designed. I am a Learning and development professional who is looking at going out on my own and establishing my own business. I would like a website designed that people would go to to check out what I do, how I do, what skills I have and how to contact me. Also room for a blog/articles.

Target Market(s)

Small to medium business

Industry/Entity Type

Self employed training and consultancy company

Number of Pages Required

5+ page

Requirements
Must have
• home page, about page, contact us page, blog page, search for us page
Nice to have
• Testimonials,

```html
<!DOCTYPE html>
<html lang="en">
<head>
<meta charset="utf-8">
<title>Tidewell Consulting</title>
<link href="https://fonts.googleapis.com/css2?family=Poppins:wght@400;500;600;700&display=swap" rel="stylesheet">
<style>
:root{
  --green:#3aa935;
  --blue:#3d8bd0;
  --link-blue:#2f56b0;
  --navy:#2b2f86;
  --ink:#1a1a1a;
  --muted:#8a8a8a;
  --line:#cfcfcf;
  --numeral:#e2e2e2;
  --dots:#eef0f6;
  --footer:#f1f1f1;
}
*{box-sizing:border-box;margin:0;padding:0}
html,body{width:1200px;height:4518px;overflow:hidden}
body{position:relative;background:#fff;font-family:'Poppins',sans-serif;color:var(--ink)}
.abs{position:absolute}
.brand{display:flex;align-items:center;gap:10px;font-weight:700;font-size:22px;color:var(--ink);letter-spacing:.5px}
.brand-dot{width:18px;height:18px;border-radius:50%;background:var(--green)}
.nav{display:flex;gap:40px;font-size:15px;color:#333}
.nav .active{color:var(--link-blue)}
.search{border:1px solid var(--line);display:flex;align-items:center;justify-content:space-between;padding:0 14px;font-size:15px;color:#888}
.btn{background:var(--green);color:#fff;font-weight:600;font-size:16px;display:flex;align-items:center;justify-content:center;border-radius:3px}
.photo{border-radius:34px;overflow:hidden}
.dots{background:var(--dots);border-radius:6px}
.numeral{font-weight:700;font-size:190px;line-height:1;color:var(--numeral);letter-spacing:-6px}
.feat-title{font-weight:500;font-size:40px;line-height:1}
.body-copy{font-size:15px;line-height:28px;color:var(--muted);text-align:justify}
.section-title{font-weight:700;font-size:42px;text-align:center;width:1200px;left:0}
.blog-title{font-weight:600;font-size:22px}
.blog-text{font-size:14px;line-height:24px;color:var(--muted)}
.read{font-size:14px;color:var(--green);font-weight:500}
.quote{width:300px;text-align:center;font-size:14px;line-height:28px;color:var(--muted)}
.quote-name{display:block;margin-top:10px;color:var(--link-blue);font-weight:600}
.avatar{width:80px;height:80px;border-radius:50%;background:linear-gradient(#b98a6c,#5b4335)}
.field{border:1px solid var(--line);font-size:15px;color:#888;padding:10px 10px}
.foot-links{display:flex;gap:0;font-size:15px;color:#666}
</style>
</head>
<body>

<!-- Header -->
<div class="abs brand" style="left:90px;top:62px"><span class="brand-dot"></span>Tidewell Consulting</div>
<nav class="abs nav" style="left:465px;top:34px">
  <span class="active">HOME</span><span>ABOUT</span><span>CONTACT</span><span>BLOG</span>
</nav>
<div class="abs search" style="left:837px;top:26px;width:272px;height:40px">Search
  <svg width="16" height="16" viewBox="0 0 16 16"><circle cx="7" cy="7" r="5" fill="none" stroke="#999" stroke-width="1.6"/><line x1="11" y1="11" x2="15" y2="15" stroke="#999" stroke-width="1.6"/></svg>
</div>

<!-- Hero -->
<div class="abs" style="left:88px;top:205px;font-weight:700;font-size:72px;line-height:1">Tidewell</div>
<div class="abs" style="left:90px;top:295px;font-size:28px;color:var(--blue)">Consulting</div>
<p class="abs" style="left:90px;top:342px;width:430px;font-size:15px;line-height:24px;color:var(--muted)">Lorem ipsum dolor sit amet, consectetur adipiscing elit, sed do eiusmod tempor incididunt</p>
<div class="abs btn" style="left:90px;top:426px;width:168px;height:48px">Get Started</div>
<div class="abs dots" role="img" aria-label="Dot grid decoration" style="left:623px;top:149px;width:184px;height:140px"></div>
<div class="abs" style="left:644px;top:239px;width:463px;height:400px;border-radius:44px;background:var(--blue)"></div>
<div class="abs" role="img" aria-label="Smiling woman holding an open laptop" style="left:580px;top:72px;width:420px;height:567px;background:linear-gradient(180deg,rgba(150,110,80,.55),rgba(235,235,240,.75) 45%,rgba(40,60,120,.6));border-radius:40px 40px 0 0"></div>

<!-- Welcome -->
<h1 class="abs section-title" style="top:726px">Welcome To Tidewell Consulting</h1>
<div class="abs" style="left:0;width:1200px;top:780px;text-align:center;font-size:17px;color:var(--link-blue)">About Us</div>

<!-- Feature 01 -->
<div class="abs" style="left:0;top:1166px;width:128px;height:237px;background:var(--navy);border-radius:0 0 14px 0"></div>
<div class="abs dots" role="img" aria-label="Dot grid decoration" style="left:39px;top:821px;width:189px;height:240px"></div>
<div class="abs" style="left:81px;top:861px;width:494px;height:472px;border-radius:34px;border:6px solid var(--blue);border-top:none;border-right:none"></div>
<div class="abs photo" role="img" aria-label="Woman writing notes at a desk" style="left:88px;top:861px;width:487px;height:463px;background:linear-gradient(135deg,#c8b8a4,#8b7a68 55%,#d9c7ad)"></div>
<div class="abs numeral" style="left:645px;top:845px">01</div>
<h2 class="abs feat-title" style="left:645px;top:982px">What I Do</h2>
<p class="abs body-copy" style="left:644px;top:1054px;width:458px">Lorem ipsum dolor sit amet, consectetur adipiscing elit, sed do eiusmod tempor incididunt ut labore et dolore magna aliqua. Ut enim ad minim veniam, quis nostrud exercitation ullamco laboris nisi ut aliquip ex ea commodo consequat. Duis aute irure dolor in reprehenderit in voluptate velit esse cillum dolore eu fugiat nulla pariatur.</p>
<div class="abs btn" style="left:645px;top:1249px;width:169px;height:49px">Read More</div>

<!-- Feature 02 -->
<div class="abs numeral" style="left:88px;top:1458px">02</div>
<h2 class="abs feat-title" style="left:91px;top:1596px">How I Do</h2>
<p class="abs body-copy" style="left:90px;top:1666px;width:458px">Lorem ipsum dolor sit amet, consectetur adipiscing elit, sed do eiusmod tempor incididunt ut labore et dolore magna aliqua. Ut enim ad minim veniam, quis nostrud exercitation ullamco laboris nisi ut aliquip ex ea commodo consequat. Duis aute irure dolor in reprehenderit in voluptate velit esse cillum dolore eu fugiat nulla pariatur.</p>
<div class="abs btn" style="left:91px;top:1861px;width:169px;height:47px">Read More</div>
<div class="abs" style="left:1070px;top:1780px;width:130px;height:234px;background:var(--navy);border-radius:14px 0 0 14px"></div>
<div class="abs dots" role="img" aria-label="Dot grid decoration" style="left:970px;top:1433px;width:188px;height:237px"></div>
<div class="abs" style="left:621px;top:1473px;width:495px;height:470px;border-radius:34px;border:6px solid var(--blue);border-top:none;border-left:none"></div>
<div class="abs photo" role="img" aria-label="Presenter speaking to a seated audience" style="left:621px;top:1473px;width:488px;height:462px;background:linear-gradient(135deg,#e4e4e4,#b9b2a8 50%,#6f6255)"></div>

<!-- Feature 03 -->
<div class="abs" style="left:0;top:2391px;width:128px;height:235px;background:var(--navy);border-radius:0 0 14px 0"></div>
<div class="abs dots" role="img" aria-label="Dot grid decoration" style="left:39px;top:2043px;width:189px;height:237px"></div>
<div class="abs" style="left:81px;top:2084px;width:494px;height:470px;border-radius:34px;border:6px solid var(--blue);border-top:none;border-right:none"></div>
<div class="abs photo" role="img" aria-label="Team meeting around a table with a presenter" style="left:88px;top:2084px;width:487px;height:461px;background:linear-gradient(135deg,#d7d7d2,#a89a88 55%,#6a5a4a)"></div>
<div class="abs numeral" style="left:645px;top:2068px">03</div>
<h2 class="abs feat-title" style="left:645px;top:2220px">Our Skills</h2>
<p class="abs body-copy" style="left:644px;top:2278px;width:458px">Lorem ipsum dolor sit amet, consectetur adipiscing elit, sed do eiusmod tempor incididunt ut labore et dolore magna aliqua. Ut enim ad minim veniam, quis nostrud exercitation ullamco laboris nisi ut aliquip ex ea commodo consequat. Duis aute irure dolor in reprehenderit in voluptate velit esse cillum dolore eu fugiat nulla pariatur.</p>
<div class="abs btn" style="left:645px;top:2471px;width:169px;height:50px">Read More</div>

<!-- Latest Blog -->
<h2 class="abs section-title" style="top:2720px">Latest Blog</h2>
<div class="abs brand" style="left:82px;top:2806px;font-size:20px"><span class="brand-dot"></span>Tidewell Consulting</div>
<svg class="abs" style="left:90px;top:3018px" width="44" height="18" viewBox="0 0 44 18">
  <path d="M10 3 L3 9 L10 15 M3 9 H17" fill="none" stroke="#888" stroke-width="2.4"/>
  <path d="M34 3 L41 9 L34 15 M41 9 H27" fill="none" stroke="var(--green)" stroke-width="2.4"/>
</svg>
<article class="abs" style="left:374px;top:2796px;width:357px">
  <div role="img" aria-label="Group discussion in an office" style="height:237px;background:linear-gradient(135deg,#6c7a6e,#c9c3b8 50%,#3e4444)"></div>
  <h3 class="blog-title" style="margin-top:14px">Lorem ipsum dolor sit amet</h3>
  <p class="blog-text" style="margin-top:10px">Lorem ipsum dolor sit amet, consectetur adipiscing elit, sed do eiusmod tempor incidi ut labore et dolore magna aliqua.</p>
  <div class="read" style="margin-top:14px">Read More</div>
</article>
<article class="abs" style="left:749px;top:2796px;width:360px">
  <div role="img" aria-label="Man talking at a desk with a monitor" style="height:237px;background:linear-gradient(135deg,#c3ccd4,#7d98b8 55%,#283f6e)"></div>
  <h3 class="blog-title" style="margin-top:14px">Lorem ipsum dolor sit amet</h3>
  <p class="blog-text" style="margin-top:10px">Lorem ipsum dolor sit amet, consectetur adipiscing elit, sed do eiusmod tempor incidi ut labore et dolore magna aliqua.</p>
  <div class="read" style="margin-top:14px">Read More</div>
</article>

<!-- Testimonials -->
<h2 class="abs section-title" style="top:3277px">Testimonials</h2>
<div class="abs avatar" role="img" aria-label="Client portrait" style="left:200px;top:3350px"></div>
<div class="abs avatar" role="img" aria-label="Client portrait" style="left:560px;top:3350px"></div>
<div class="abs avatar" role="img" aria-label="Client portrait" style="left:920px;top:3350px;background:linear-gradient(#c98a5a,#7a4b35)"></div>
<p class="abs quote" style="left:90px;top:3447px">Lorem ipsum dolor sit amet, consectetur adipiscing elit, sed do eiusmod tempor incididunt ut labore et dolore<span class="quote-name">-Ana Rewiti</span></p>
<p class="abs quote" style="left:450px;top:3447px">Lorem ipsum dolor sit amet, consectetur adipiscing elit, sed do eiusmod tempor incididunt ut labore et dolore<span class="quote-name">-Ana Rewiti</span></p>
<p class="abs quote" style="left:810px;top:3447px">Lorem ipsum dolor sit amet, consectetur adipiscing elit, sed do eiusmod tempor incididunt ut labore et dolore<span class="quote-name">-Ana Rewiti</span></p>

<!-- Contact -->
<h2 class="abs" style="left:90px;top:3726px;font-weight:700;font-size:42px">Contact Us</h2>
<div class="abs field" style="left:90px;top:3815px;width:271px;height:40px">Last Name</div>
<div class="abs field" style="left:374px;top:3815px;width:271px;height:40px">Last Name</div>
<div class="abs field" style="left:90px;top:3870px;width:271px;height:42px">Phone Number</div>
<div class="abs field" style="left:374px;top:3870px;width:271px;height:42px">Email</div>
<div class="abs field" style="left:90px;top:3925px;width:271px;height:41px">Address</div>
<div class="abs field" style="left:374px;top:3925px;width:271px;height:41px">Subject</div>
<div class="abs field" style="left:90px;top:3978px;width:555px;height:107px">Message</div>
<div class="abs btn" style="left:90px;top:4101px;width:168px;height:47px">Submit</div>
<div class="abs dots" role="img" aria-label="Dot grid decoration" style="left:995px;top:3648px;width:184px;height:237px"></div>
<div class="abs photo" role="img" aria-label="Woman working on a laptop" style="left:663px;top:3706px;width:444px;height:474px;background:linear-gradient(135deg,#5a5450,#d6a070 50%,#e9e7e4)"></div>

<!-- Footer -->
<footer class="abs" style="left:0;top:4280px;width:1200px;height:238px;background:var(--footer)">
  <div class="abs brand" style="left:0;width:1200px;justify-content:center;top:50px"><span class="brand-dot"></span>Tidewell Consulting</div>
  <div class="abs foot-links" style="left:390px;top:146px">
    <span style="width:112px">HOME</span><span style="width:141px">ABOUT US</span><span style="width:124px">CONTACT US</span><span>BLOG</span>
  </div>
  <div class="abs" style="left:0;width:1200px;text-align:center;top:194px;font-size:12px;color:#777">© Copyright 2021 The Company name. All Rights Reserved.</div>
</footer>

</body>
</html>
```